BEREAN FELLOWSHIP GLOBAL.

THIS IS A PRAISE AND WORSHIP MEETING, WORTH NOTING, THAT ITS OUR FIRST MEETING. OUR THEME AND VISION......" Building A Bridge Of Fellowship Between Man And God". This should stand out. We also have a logo and I will email it to the designer that takes the job. We will have three pictures on the flier. Red is favourite color........ DATE OF THE MEETING. Saturday NOV 11th 2017. 6:30pm-9pm. Venue LAMPSTAND HARVEST CHAPEL 27108 Orchard RD N, Auburn Wa 98001. Punch line at the bottom.....' the PRAISE to be'

Target Market(s)

Youth and adults.

Industry/Entity Type

Performing Art

Font styles to use
Decorative

Colors

Designer to choose colors to be used in the design.

Requirements
Must have
• The first design of the attached Logo. And the words......BUILDING A BRIDGE OF FELLOWSHIP BETWEEN MAN AND GOD.
Should not have
• Pictures of three individuals. I have one but waiting for 2. I can send them later. The picture that is attached is of Samuel T Wekesa.

```html
<!DOCTYPE html>
<html lang="en">
<head>
<meta charset="utf-8">
<title>The Praise To Be — Meeting Flyer</title>
<link rel="stylesheet" href="https://fonts.googleapis.com/css2?family=Rye&family=Cinzel:wght@400&family=Open+Sans:wdth,wght@75..100,400..700&family=Stardos+Stencil:wght@400&display=swap">
<style>
  :root {
    --stage: #a9a9a7;
    --sky-top: #d9432f;
    --sky-mid: #c9402f;
    --sky-low: #e0562c;
    --panel-red: #c8363a;
    --white: #ffffff;
    --gold: #fcd116;
    --ink: #111111;
    --photo-a: #3b3f57;
    --photo-b: #5a5f78;
  }
  * { margin: 0; padding: 0; box-sizing: border-box; }
  html, body { width: 1200px; height: 1200px; overflow: hidden; }
  body { background: var(--stage); position: relative; }

  .flyer {
    position: absolute;
    left: 198px; top: 31px;
    width: 855px; height: 1211px;
    transform: scale(0.94);
    transform-origin: top left;
    overflow: hidden;
    background: radial-gradient(ellipse at 50% 35%, var(--sky-low) 0%, var(--sky-mid) 55%, var(--sky-top) 100%);
  }
  .flyer__art { position: absolute; inset: 0; width: 855px; height: 1211px; }

  .headline {
    position: absolute; left: 0; right: 0; top: 36px;
    text-align: center;
    font-family: "Rye", serif;
    color: var(--white);
    line-height: 1;
    font-weight: 400;
  }
  .headline__line { display: block; font-size: 50px; letter-spacing: 1px; margin-bottom: 8px; }
  .headline__focus { display: block; color: var(--gold); font-size: 92px; letter-spacing: 2px; margin-top: 6px; }

  .brand {
    position: absolute; left: 36px; top: 727px;
    display: flex; align-items: center; gap: 20px;
  }
  .brand__mark { width: 96px; height: 96px; border-radius: 50%; border: 4px solid var(--white); flex: none; }
  .brand__name {
    font-family: "Cinzel", serif; font-weight: 400;
    color: var(--white); font-size: 30px; line-height: 1.05; letter-spacing: 1px;
  }
  .brand__tagline {
    position: absolute; left: 154px; top: 801px;
    font-family: "Open Sans", sans-serif; font-size: 10px; color: var(--white);
    border-top: 1px solid var(--white); padding-top: 4px; width: 285px;
  }

  .event-title {
    position: absolute; left: 60px; top: 858px;
    font-family: "Rye", serif; font-weight: 400; color: var(--white); font-size: 46px; letter-spacing: 1px;
  }
  .details {
    position: absolute; left: 60px; top: 922px;
    font-family: "Open Sans", sans-serif; font-stretch: 90%; font-weight: 600;
    font-size: 29px; color: var(--white); line-height: 1.2;
  }
  .details__row { margin-bottom: 6px; }
  .details__label { color: var(--gold); }
  .details sup { font-size: 16px; }

  .punchline {
    position: absolute; left: 0; right: 0; bottom: 0; height: 86px;
    background: var(--gold);
    display: flex; align-items: center; justify-content: center;
    font-family: "Stardos Stencil", serif; font-weight: 400;
    font-size: 46px; letter-spacing: 8px; color: var(--ink);
  }
</style>
</head>
<body>
  <main class="flyer">
    <svg class="flyer__art" viewBox="0 0 855 1211">
      <defs>
        <linearGradient id="portraitFill" x1="0" y1="0" x2="0" y2="1">
          <stop offset="0" stop-color="#5a5f78"/>
          <stop offset="1" stop-color="#3b3f57"/>
        </linearGradient>
      </defs>
      <g class="sunburst" fill="#ffffff" opacity="0.09">
        <polygon points="400,430 855,250 855,330"/>
        <polygon points="400,430 855,400 855,470"/>
        <polygon points="400,430 855,540 855,610"/>
        <polygon points="400,430 855,690 820,760"/>
        <polygon points="400,430 0,250 0,320"/>
        <polygon points="400,430 0,410 0,470"/>
        <polygon points="400,430 0,560 0,620"/>
        <polygon points="400,430 560,0 640,0"/>
        <polygon points="400,430 200,0 270,0"/>
        <polygon points="400,430 60,0 130,0"/>
      </g>
      <rect class="portrait" role="img" aria-label="Photo of the guest minister, smiling with arms folded in a dark paisley shirt"
            x="240" y="265" width="445" height="520" rx="40" fill="url(#portraitFill)"/>
      <path class="curve-band" d="M0,700 C120,630 330,620 520,720 C640,785 760,880 855,925 L855,1211 L0,1211 Z" fill="#ffffff"/>
      <path class="info-panel" d="M0,728 C130,660 330,648 515,742 C640,808 760,895 855,935 L855,1211 L0,1211 Z" fill="#c8363a"/>
    </svg>

    <h1 class="headline">
      <span class="headline__line">BUILDING A BRIDGE OF</span>
      <span class="headline__line">FELLOWSHIP BETWEEN</span>
      <span class="headline__focus">MAN AND GOD</span>
    </h1>

    <div class="brand">
      <span class="brand__mark"></span>
      <span class="brand__name">BEREAN FELLOWSHIP<br>GLOBAL</span>
    </div>
    <p class="brand__tagline">Building A Bridge Of Fellowship Between Man And God</p>

    <h2 class="event-title">MEETING</h2>
    <div class="details">
      <p class="details__row"><span class="details__label">DATE:</span> SATURDAY NOV 11<sup>TH</sup> 2017</p>
      <p class="details__row"><span class="details__label">TIME:</span> 6:30PM-9PM</p>
      <p class="details__row"><span class="details__label">VENUE:</span> LAMPSTAND HARVEST CHAPEL 27108<br>ORCHARD RD N, AUBURN WA 98001</p>
    </div>

    <footer class="punchline">THE PRAISE TO BE</footer>
  </main>
</body>
</html>
```